An Iconic transformation in mattress design and comfort.

“An iconic transformation in mattress design and comfort”
We are Not Kidding here!!
This is an upstart Company, BRIMO7, LLC
Our Slogan
“rest-BRIMO”

We need an outstanding web design for an outstanding product.

It took 8 years to design this bed. It was originally designed by its owner for its owner, I continue to use it every day.

With our innovative patent pending support system, with quality throughout, simplicity in design, affordable, and proudly made here in the USA, we offer a product that is superior to anything that is in the market place now. The materials that are used deviate from the industry standard, and for good reason, our product feels incredibly plush, soft, but yet provides support that can be adjusted in a simple manor, a product that will last a lifetime.
Really, why go to work if you can lay in this bed all day; you'll want to work from home! A quick nap, you'll be in heaven.

Overall Web design:
We like the web site “quietwhorl.example”, sleek, modern, a site that seems to add credibility to their product by issuing registration numbers for their tops, not a bad idea for our beds. Its important to understand that this industry is filled with smoke and mirrors, over pricing, very poor quality, and show rooms filled with sales people that are piranhas.; we seek to distance ourselves! This company will sell its product not in the traditional show room but online. Please also see these websites: www.dunelayer.example, www.tarnwick.example

Last thing I want to see is a another website filled with beds, what to do? Well perhaps a few shots of our beds is ok, after all thats what we are selling. An idea here; I was listening to a news show, this man decided to tell his story with tattoos on his own body! Interesting, different approach (not that I'm into tattoos); website design with innovation through simplicity and creative thinking and marketing.

The photos of our product have yet to be taken by a professional. We have yet to find a way to photograph this product in a different and innovative manner.

Target Market(s)

Millennials

Industry/Entity Type

It Company

Number of Pages Required

4 page

Font styles to use
Serif

Colors
ec1f27

Requirements
Must have
• Existing logo
Nice to have
• See project description
• Can further expand upon, upon request for specifics.
Should not have
• See project description

```html
<!DOCTYPE html>
<html lang="en">
<head>
<meta charset="utf-8">
<title>BRIMO7 — rest-BRIMO</title>
<link href="https://fonts.googleapis.com/css2?family=Jost:wght@400;500&family=Open+Sans:ital,wght@0,400;0,600;0,700;1,400&display=swap" rel="stylesheet">
<style>
:root{
  --red:#c1272d;
  --ink:#222222;
  --text:#555555;
  --muted:#777777;
  --panel:#f2f2f2;
  --line:#dddddd;
  --white:#ffffff;
  --hero-a:#6b5a48;
  --hero-b:#d9d2c4;
}
*{box-sizing:border-box;margin:0;padding:0}
html,body{width:1200px;height:2844px;overflow:hidden;background:var(--white)}
body{font-family:"Open Sans",Arial,sans-serif;color:var(--text);position:relative}
.heading{font-family:"Jost","Futura",sans-serif;font-weight:400;color:var(--ink)}
a{color:inherit;text-decoration:none}

/* header */
.site-header{position:absolute;top:0;left:0;width:1200px;height:88px;border-top:4px solid var(--red);background:var(--white)}
.brand{position:absolute;left:98px;top:14px;font-family:"Jost",sans-serif;color:var(--ink)}
.brand-name{font-size:40px;font-weight:500;line-height:42px;letter-spacing:1px}
.brand-tag{font-size:13px;line-height:14px;margin-left:40px}
.main-nav{position:absolute;left:338px;top:32px;display:flex;gap:30px;font-family:"Jost",sans-serif;font-size:17px;color:var(--ink)}
.nav-search{position:absolute;left:828px;top:34px}
.phone{position:absolute;left:872px;top:27px;display:flex;align-items:center;gap:12px;font-family:"Jost",sans-serif;font-size:19px;color:var(--ink)}
.phone-ring{width:32px;height:32px;border:1.5px solid var(--line);border-radius:50%;display:flex;align-items:center;justify-content:center}
.cart{position:absolute;left:1062px;top:33px;font-size:12px;color:var(--muted);display:flex;gap:5px;align-items:center}

/* hero */
.hero{position:absolute;top:88px;left:0;width:1200px;height:447px;background:linear-gradient(180deg,var(--hero-a) 0%,#8d7a63 45%,var(--hero-b) 62%,#5b5a60 80%,#3f3f45 100%)}
.hero-slogan{position:absolute;top:168px;width:100%;text-align:center;font-family:"Jost",sans-serif;font-size:78px;color:var(--white);letter-spacing:2px}
.hero-slogan .dash{display:inline-block;width:110px;height:6px;background:var(--red);border-radius:3px;vertical-align:middle;margin:0 24px}
.hero-dots{position:absolute;top:386px;left:568px;display:flex;gap:6px}
.hero-dots span{width:11px;height:11px;border-radius:50%;border:1.5px solid var(--white)}
.hero-dots span.active{background:var(--white)}

/* welcome */
.welcome{position:absolute;top:535px;left:0;width:1200px;height:583px}
.section-title{font-size:42px;text-align:center}
.welcome .section-title{margin-top:50px}
.lead{width:680px;margin:20px auto 0;text-align:center;font-size:12.5px;line-height:25px}
.features{position:absolute;top:222px;left:0;width:1200px}
.feature{position:absolute;width:300px;text-align:center}
.feature svg{display:block;margin:0 auto}
.feature-title{font-family:"Jost",sans-serif;font-size:21px;color:var(--ink);margin-top:50px}
.feature p{font-size:12px;line-height:21px;margin-top:12px}
.read-link{display:block;margin-top:18px;font-size:12.5px;font-weight:700;color:var(--red)}

/* perfect mattress */
.perfect{position:absolute;top:1118px;left:0;width:1200px;height:456px;background:var(--panel)}
.perfect-photo{position:absolute;left:0;top:0;width:600px;height:456px;background:linear-gradient(180deg,#8a7d5c 0%,#c9bf96 45%,#f2efe6 62%,#3b3b42 80%,#2d2d33 100%)}
.perfect-body{position:absolute;left:654px;top:30px;width:500px}
.perfect-body h2{font-size:40px}
.perfect-body p{font-size:12px;line-height:22px;margin-top:20px}
.perks{display:grid;grid-template-columns:238px 238px;row-gap:28px;margin-top:28px}
.perk{display:flex;align-items:center;gap:20px;font-family:"Jost",sans-serif;font-size:20px;color:var(--ink)}
.perk-ring{width:66px;height:66px;border:1.5px solid #cccccc;border-radius:50%;display:flex;align-items:center;justify-content:center;background:var(--white)}
.btn-outline{display:inline-block;border:1.5px solid #999999;padding:10px 22px;font-size:12.5px;font-weight:700;color:var(--red)}
.perfect .btn-outline{margin-top:38px}

/* testimonials */
.testimonials{position:absolute;top:1574px;left:0;width:1200px;height:457px;text-align:center}
.testimonials .section-title{margin-top:54px}
.avatar{width:122px;height:122px;border-radius:50%;border:4px solid #e4e4e4;margin:32px auto 0;background:linear-gradient(160deg,#b9aa9a,#7d6e62)}
.quote{font-style:italic;font-size:13.5px;line-height:28px;width:700px;margin:22px auto 0;color:#666666}
.quote-author{margin-top:16px;font-size:14.5px;font-weight:700;color:var(--red)}

/* about */
.about{position:absolute;top:2031px;left:98px;width:1003px;height:403px;background:var(--panel);border:1px solid var(--line)}
.about-body{position:absolute;left:48px;top:40px;width:630px}
.about-body h2{font-size:42px}
.about-body p{font-size:12px;line-height:26.5px;margin-top:20px}
.about .btn-outline{margin-top:26px}
.about-photo{position:absolute;right:-1px;top:-1px;width:306px;height:403px;background:radial-gradient(ellipse at 55% 65%,#f1ece6 0%,#c9bfb3 40%,#3a2f2a 85%)}

/* footer */
.site-footer{position:absolute;top:2503px;left:0;width:1200px;height:341px;border-top:5px solid var(--red)}
.foot-col{position:absolute;top:48px}
.foot-col h3{font-family:"Jost",sans-serif;font-weight:500;font-size:18px;color:var(--ink)}
.foot-col ul{list-style:none;margin-top:14px}
.foot-col li{font-size:12px;line-height:26.5px;color:var(--text)}
.col-divider{position:absolute;top:40px;width:1px;height:210px;background:var(--line)}
.subscribe-note{font-size:12px;margin-top:16px}
.subscribe{display:flex;margin-top:14px}
.subscribe .field{width:228px;height:35px;border:1px solid var(--line);font-size:12px;line-height:33px;padding-left:12px;color:var(--muted)}
.subscribe .submit{width:96px;height:35px;background:var(--red);color:var(--white);font-weight:700;font-size:12.5px;text-align:center;line-height:35px}
.stay{margin-top:14px}
.social{display:flex;gap:13px;margin-top:16px}
.social span{width:34px;height:34px;border-radius:50%}
.foot-rule{position:absolute;top:270px;left:98px;width:1003px;height:1px;background:var(--line)}
.legal{position:absolute;top:298px;width:100%;text-align:center;font-size:11.5px;color:var(--text)}
</style>
</head>
<body>

<header class="site-header">
  <div class="brand"><div class="brand-name">BRIMO7</div><div class="brand-tag">rest-BRIMO</div></div>
  <nav class="main-nav"><a>Mattress</a><a>About</a><a>Reviews</a><a>Compare</a><a>FAQ</a><a>Contact</a></nav>
  <svg class="nav-search" width="18" height="18" viewBox="0 0 18 18"><circle cx="7.5" cy="7.5" r="5.5" fill="none" stroke="#222" stroke-width="2"/><line x1="11.5" y1="11.5" x2="16" y2="16" stroke="#222" stroke-width="2.4" stroke-linecap="round"/></svg>
  <div class="phone"><span class="phone-ring"><svg width="14" height="14" viewBox="0 0 24 24"><path d="M6.6 10.8a15 15 0 0 0 6.6 6.6l2.2-2.2c.3-.3.7-.4 1-.2 1.1.4 2.3.6 3.6.6.6 0 1 .4 1 1V20c0 .6-.4 1-1 1A17 17 0 0 1 3 4c0-.6.4-1 1-1h3.5c.6 0 1 .4 1 1 0 1.3.2 2.5.6 3.6.1.3 0 .7-.2 1z" fill="#c1272d"/></svg></span>1 888 888 888</div>
  <div class="cart"><svg width="18" height="16" viewBox="0 0 24 20"><path d="M1 2h4l3 11h12l3-8H7" fill="none" stroke="#c1272d" stroke-width="2.4"/><circle cx="9" cy="17" r="2" fill="#c1272d"/><circle cx="19" cy="17" r="2" fill="#c1272d"/></svg>(0)</div>
</header>

<section class="hero" role="img" aria-label="Mattress photographed on a carpet in a living room by a fireplace">
  <div class="hero-slogan">rest<span class="dash"></span>BRIMO</div>
  <div class="hero-dots"><span class="active"></span><span></span><span></span><span></span></div>
</section>

<section class="welcome">
  <h1 class="heading section-title">Welcome to BRIMO7</h1>
  <p class="lead">With our innovative patent pending support system, with quality throughout, simplicity in design, affordable, and proudly made here in the USA, we offer a product that is superior to anything that is in the market place now.</p>
  <div class="features">
    <div class="feature" style="left:78px">
      <svg width="152" height="110" viewBox="0 0 152 110" fill="none" stroke="#c1272d" stroke-width="2.5" stroke-linejoin="round"><path d="M14 56V14c0-6 4-10 10-10h104c6 0 10 4 10 10v42"/><rect x="28" y="30" width="42" height="22" rx="6"/><rect x="82" y="30" width="42" height="22" rx="6"/><rect x="6" y="56" width="140" height="30" rx="4"/><path d="M14 86v16M138 86v16"/></svg>
      <div class="feature-title">Proudly Made</div>
      <p>At vero eos et accusamus et iusto odio dignis mos ducimus qui blanditiis praesentium volupta tum deleniti atque corruptiqu</p>
      <a class="read-link">READ MORE</a>
    </div>
    <div class="feature" style="left:450px">
      <svg width="150" height="150" viewBox="0 0 150 150" fill="none" stroke="#c1272d" stroke-width="2.5" style="margin-top:-22px;margin-bottom:-18px"><path d="M75 6l12 10 15-4 6 14 15 4-2 15 10 12-10 12 2 15-15 4-6 14-15-4-12 10-12-10-15 4-6-14-15-4 2-15-10-12 10-12-2-15 15-4 6-14 15 4z"/><circle cx="75" cy="75" r="26"/><path d="M63 75l9 9 17-18" stroke-width="3"/></svg>
      <div class="feature-title">Limited Warranty</div>
      <p>At vero eos et accusamus et iusto odio dignis mos ducimus qui blanditiis praesentium volupta tum deleniti atque corruptiqu</p>
      <a class="read-link">READ MORE</a>
    </div>
    <div class="feature" style="left:817px">
      <svg width="176" height="110" viewBox="0 0 176 110" fill="none" stroke="#c1272d" stroke-width="2.5" stroke-linejoin="round"><path d="M120 6h52M130 20h40M140 34h30M120 48h44M132 62h34"/><rect x="52" y="16" width="66" height="62"/><path d="M52 40H24L10 60v18h42"/><path d="M18 60h22V46"/><circle cx="30" cy="84" r="9"/><circle cx="98" cy="84" r="9"/></svg>
      <div class="feature-title">Direct Delivery</div>
      <p>At vero eos et accusamus et iusto odio dignis mos ducimus qui blanditiis praesentium volupta tum deleniti atque corruptiqu</p>
      <a class="read-link">READ MORE</a>
    </div>
  </div>
</section>

<section class="perfect">
  <div class="perfect-photo" role="img" aria-label="Side view of the mattress with its quilted grey border in front of a fireplace"></div>
  <div class="perfect-body">
    <h2 class="heading">The Perfect Mattress</h2>
    <p>Nam libero tempore, cum soluta nobis est eligendi optio cumque nihil impedit e quo minus id quod maxime placeat facere possi.</p>
    <div class="perks">
      <div class="perk"><span class="perk-ring"><svg width="26" height="26" viewBox="0 0 26 26"><circle cx="13" cy="13" r="12" fill="#c1272d"/><path d="M7.5 13.5l4 4 7-8" fill="none" stroke="#fff" stroke-width="2.6"/></svg></span>Simplicity</div>
      <div class="perk"><span class="perk-ring"><svg width="28" height="28" viewBox="0 0 28 28"><path d="M3 4h11l11 11-10 10L4 14z" fill="#c1272d"/><circle cx="9" cy="9" r="2.2" fill="#fff"/></svg></span>Affordable</div>
      <div class="perk"><span class="perk-ring"><svg width="28" height="28" viewBox="0 0 28 28"><path d="M14 2l3.6 7.6 8.2 1-6 5.7 1.5 8.2L14 20.5l-7.3 4 1.5-8.2-6-5.7 8.2-1z" fill="#c1272d"/></svg></span>Proudly Made</div>
      <div class="perk"><span class="perk-ring"><svg width="26" height="26" viewBox="0 0 26 26"><rect x="2" y="11" width="5" height="13" fill="#c1272d"/><path d="M9 11l5-9c2 0 3 1 3 3l-1 5h7c1.5 0 2.5 1.3 2 2.7l-3 9c-.3 1-1.2 1.8-2.3 1.8H9z" fill="#c1272d"/></svg></span>Quality</div>
    </div>
    <a class="btn-outline">READ MORE</a>
  </div>
</section>

<section class="testimonials">
  <h2 class="heading section-title">Client Testimonials</h2>
  <div class="avatar" role="img" aria-label="Portrait of the customer"></div>
  <p class="quote">" At vero eos et accusamus et iusto odio dignissimos ducimus qui blanditiis praesentium voluptatum deleniti atque corrupti quos dolores et quas molestias excepturi sint occaecati cupiditate non provident, similique sunt in culpa qui officia deserunt mollitia animi, id est "</p>
  <div class="quote-author">- DAVID HALE</div>
</section>

<section class="about">
  <div class="about-body">
    <h2 class="heading">About BRIMO7</h2>
    <p>It took 8 years to design this bed. It was originally designed by its owner for its owner, I continue to use it every day. With our innovative patent pending support system, with quality throughout, simplicity in design, affordable, and proudly made here in the USA, we offer a product that is superior to anything that is in the market place now. The materials that are used deviate from the industry standard, and for good reason, our product feels incredibly plush, soft, but yet provides support that can be adjusted in a simple manor, a product that will last a lifetime. Really, why go to work if you can lay in this bed all day; you'll want to work from home! A quick nap, you'll be in heaven.</p>
    <a class="btn-outline">READ MORE</a>
  </div>
  <div class="about-photo" role="img" aria-label="Close-up of the plush white mattress top in a dim bedroom"></div>
</section>

<footer class="site-footer">
  <div class="foot-col" style="left:98px"><h3>Resources</h3><ul><li>Learn</li><li>Community</li><li>Documentation</li><li>FAQ</li><li>Services Status</li><li>Certification</li></ul></div>
  <div class="col-divider" style="left:246px"></div>
  <div class="foot-col" style="left:294px"><h3>Help &amp; support</h3><ul><li>Recommended Reading</li><li>Submit your Story</li><li>Contact Us</li><li>Frequently Asked Questions</li><li>How to Order</li></ul></div>
  <div class="col-divider" style="left:506px"></div>
  <div class="foot-col" style="left:554px"><h3>Quick Links</h3><ul><li>Blog</li><li>Events</li><li>Careers</li><li>Press</li><li>Contact</li><li>Partners</li></ul></div>
  <div class="col-divider" style="left:714px"></div>
  <div class="foot-col" style="left:777px">
    <h3>Email Subscription</h3>
    <p class="subscribe-note">Register your email address to get information about us</p>
    <div class="subscribe"><div class="field">Email Address</div><div class="submit">SUBSCRIBE</div></div>
    <h3 class="stay">Stay Connected</h3>
    <div class="social">
      <span style="background:#4caf7a"></span><span style="background:#3b5998"></span><span style="background:#4ba7e0"></span><span style="background:#d9473a"></span><span style="background:#4f7aa3"></span><span style="background:#3aa0d8"></span><span style="background:#c4302b"></span><span style="background:#c8232c"></span>
    </div>
  </div>
  <div class="foot-rule"></div>
  <div class="legal">Copyrights © 2017, BRIMO7. All Rights Reserved &nbsp;|&nbsp; Privacy Policy | Terms of Use | Feedback</div>
</footer>

</body>
</html>
```